Brookmere Osteopathy flyer

I want a clean clear DL flyer (but also want an A4 poster) promoting a new Osteopathic business in a semi rural area in Tasmania (Australia).
It can have pictures like the examples attached to show people what Osteopathy is (its like Chiropractic and physiotherapy).
I am the sole practioner and am male, so any pictures would be best to be a white male if possible.
I've attached some wording, you can use all, or none of it
I don't have a phone number for the business yet
info@brookmereosteopathy.example
www.brookmereosteopathy.example
Target Market(s)
Australians, from tradies, professionals, babies to retired people
Industry/Entity Type
Health
Look and feel

```html
<!DOCTYPE html>
<html lang="en">
<head>
<meta charset="utf-8">
<title>Brookmere Osteopathy – DL Flyer</title>
<link rel="stylesheet" href="https://fonts.googleapis.com/css2?family=Roboto:wght@700;900&family=Roboto+Condensed:wght@700&family=Mulish:wght@600;700&display=swap">
<style>
  :root{
    --page:#7a7a7a;
    --paper:#ffffff;
    --blue:#1096d4;
    --blue-deep:#0b7fbd;
    --orange:#f5913a;
    --ink:#1a1a1a;
    --white:#ffffff;
  }
  *{box-sizing:border-box;margin:0;padding:0}
  html,body{width:1200px;height:904px;overflow:hidden;background:var(--page)}
  .canvas{position:relative;width:1200px;height:904px}
  .flyer{position:absolute;left:400px;top:22px;width:400px;height:860px;background:var(--paper);overflow:hidden;box-shadow:0 4px 14px rgba(0,0,0,.25)}
  .hero{position:absolute;left:0;top:0;width:400px;height:260px}
  .brand-mark{position:absolute;left:42px;top:120px;width:136px;height:136px;border-radius:50%;background:var(--white);border:3px solid var(--blue);display:flex;align-items:center;justify-content:center;text-align:center}
  .brand-name{font-family:"Roboto",sans-serif;font-weight:700;font-size:15px;line-height:1.2;color:var(--blue);letter-spacing:.5px;text-transform:uppercase}
  .headline{position:absolute;left:24px;top:263px;width:230px;font-family:"Roboto",sans-serif;font-weight:900;font-size:21.5px;line-height:1.24;color:var(--ink);text-transform:uppercase;white-space:nowrap}
  .tile{position:absolute;width:108px;height:96px;border-radius:4px;display:flex;flex-direction:column;align-items:center;justify-content:flex-end;padding-bottom:8px;color:var(--white);font-family:"Roboto Condensed",sans-serif;font-weight:700;font-size:12px;line-height:1.25;text-align:center}
  .tile.blue{background:var(--blue)}
  .tile.orange{background:var(--orange)}
  .tile-icon{width:44px;height:46px;border-radius:6px;background:rgba(255,255,255,.22);margin-bottom:auto;margin-top:9px}
  .tile.single-line{padding-bottom:16px}
  .c1{left:26px}.c2{left:144px}.c3{left:262px}
  .r0{top:248px}.r1{top:353px}.r2{top:460px}.r3{top:566px}
  .intro{position:absolute;left:26px;top:672px;width:344px;font-family:"Mulish",sans-serif;font-weight:600;font-size:12.4px;line-height:1.3;color:var(--ink);text-align:justify}
  .footer-band{position:absolute;left:0;top:742px;width:400px;height:118px}
  .cta{position:absolute;left:26px;top:806px;font-family:"Mulish",sans-serif;color:var(--white)}
  .cta-title{font-weight:700;font-size:17.5px;letter-spacing:.3px;text-transform:uppercase;line-height:1.1}
  .cta-phone{display:flex;align-items:center;gap:5px;font-weight:600;font-size:16.5px;margin-top:3px}
  .contact-list{position:absolute;left:182px;top:800px;list-style:none;font-family:"Mulish",sans-serif;font-weight:700;font-size:10.4px;color:var(--white);line-height:16px}
  .contact-list li{display:flex;align-items:center;gap:5px}
  .dot-icon{width:11px;height:11px;flex:none}
</style>
</head>
<body>
<div class="canvas">
  <article class="flyer">
    <svg class="hero" viewBox="0 0 400 260">
      <defs>
        <linearGradient id="photoTone" x1="0" y1="0" x2="1" y2="1">
          <stop offset="0" stop-color="#e9eef3"/>
          <stop offset=".45" stop-color="#d9b8a4"/>
          <stop offset=".75" stop-color="#c9d5e3"/>
          <stop offset="1" stop-color="#1e2b3a"/>
        </linearGradient>
      </defs>
      <rect role="img" aria-label="Photo: osteopath gently treating a patient's neck on a treatment table" x="0" y="0" width="400" height="240" fill="url(#photoTone)"/>
      <path d="M0,226 C70,200 150,214 240,206 C310,200 360,184 400,172 L400,260 L0,260 Z" fill="var(--paper)"/>
      <path d="M0,220 C70,194 150,208 240,200 C310,194 360,178 400,166 L400,180 C360,192 310,208 240,214 C150,222 70,210 0,234 Z" fill="var(--blue)"/>
    </svg>

    <div class="brand-mark">
      <span class="brand-name">Brookmere<br>Osteopathy</span>
    </div>

    <h1 class="headline">Common reasons<br>people visit<br>an osteopath:</h1>

    <div class="tile orange c3 r0"><span class="tile-icon" role="img" aria-label="Icon: back and neck pain"></span>Back /<br>neck pain</div>

    <div class="tile blue c1 r1"><span class="tile-icon" role="img" aria-label="Icon: headache"></span>Headaches<br>/ migraines</div>
    <div class="tile orange c2 r1"><span class="tile-icon" role="img" aria-label="Icon: flexed arm muscle"></span>Joint and<br>muscle pain</div>
    <div class="tile blue c3 r1"><span class="tile-icon" role="img" aria-label="Icon: pregnancy"></span>Pregnancy-related<br>discomfort</div>

    <div class="tile orange c1 r2"><span class="tile-icon" role="img" aria-label="Icon: spinal disc"></span>Disc related<br>issues</div>
    <div class="tile blue c2 r2 single-line"><span class="tile-icon" role="img" aria-label="Icon: hip and sciatic nerve"></span>Sciatica</div>
    <div class="tile orange c3 r2 single-line"><span class="tile-icon" role="img" aria-label="Icon: foot heel pain"></span>Plantar fasciitis</div>

    <div class="tile blue c1 r3"><span class="tile-icon" role="img" aria-label="Icon: knee joint"></span>Tendonitis<br>/ Bursitis</div>
    <div class="tile orange c2 r3"><span class="tile-icon" role="img" aria-label="Icon: shoulder"></span>Adhesive capsulitis<br>(frozen shoulder)</div>
    <div class="tile blue c3 r3"><span class="tile-icon" role="img" aria-label="Icon: elbow"></span>Tennis /<br>Golfers elbow</div>

    <p class="intro">Osteopaths use a combination of joint manipulation, targeted deep tissue massage &amp; stretching to improve function, relieve pain and support the body’s ability to heal itself.</p>

    <svg class="footer-band" viewBox="0 0 400 118" aria-hidden="true">
      <path d="M0,24 C90,6 170,-2 250,4 C320,10 370,26 400,36 L400,118 L0,118 Z" fill="var(--blue)"/>
      <path d="M0,36 C90,20 170,12 250,16 C320,22 368,38 400,46 L400,50 C368,42 320,28 250,22 C170,18 90,28 0,42 Z" fill="var(--paper)" opacity=".9"/>
    </svg>

    <div class="cta">
      <div class="cta-title">Call us today</div>
      <div class="cta-phone">
        <svg class="dot-icon" style="width:15px;height:15px" viewBox="0 0 16 16" aria-hidden="true"><circle cx="8" cy="8" r="8" fill="var(--orange)"/><path d="M5.2 4.2l1.4-.4.9 2-1 .8c.4 1 1.2 1.8 2.2 2.2l.8-1 2 .9-.4 1.4c-3.4.3-6.2-2.5-5.9-5.9z" fill="var(--white)"/></svg>
        (03) 5550 0142
      </div>
    </div>

    <ul class="contact-list">
      <li><svg class="dot-icon" viewBox="0 0 12 12" aria-hidden="true"><circle cx="6" cy="6" r="6" fill="var(--orange)"/><path d="M6 2.5a2 2 0 0 0-2 2c0 1.5 2 4 2 4s2-2.5 2-4a2 2 0 0 0-2-2z" fill="var(--white)"/></svg>48 Willow Creek road, Brookmere</li>
      <li><svg class="dot-icon" viewBox="0 0 12 12" aria-hidden="true"><circle cx="6" cy="6" r="6" fill="var(--orange)"/><rect x="3" y="4" width="6" height="4" fill="none" stroke="var(--white)" stroke-width=".9"/></svg>www.brookmereosteopathy.example</li>
      <li><svg class="dot-icon" viewBox="0 0 12 12" aria-hidden="true"><circle cx="6" cy="6" r="6" fill="var(--orange)"/><circle cx="6" cy="6" r="3" fill="none" stroke="var(--white)" stroke-width=".9"/></svg>info@brookmereosteopathy.example</li>
    </ul>
  </article>
</div>
</body>
</html>
```